Crest of Morning Paddocks Business Cards with logo

Need a creative business card that pops. Colorful but professional. The attached logo should be included. We are a national horse racing partnership so we are in the equine business. Nothing cartoonlike or whimsical.

Target Market(s)

professionals - 40+

Contact Information for Business Card

Maren Dunleavy
Director of Operations
27 Ashbrook Lane
Middletown, MD. 21584

Phone (313) 555-0147

FX: (949) 555-0192

email: maren@cmpaddocks.example
cmpaddocks.example

Requirements
Must have
• All information above should be on the business card including the website address. Professional yet creative
Nice to have
• an attention grabbing design. not boring. exciting.
Should not have
• cartoon like - whimsical.

```html
<!DOCTYPE html>
<html lang="en">
<head>
<meta charset="utf-8">
<title>Crest of Morning Paddocks – Business Cards</title>
<link rel="stylesheet" href="https://fonts.googleapis.com/css2?family=Source+Serif+4:opsz,wght@8..60,400;8..60,700&display=swap">
<style>
  :root {
    --backdrop: #e8e8e8;
    --paper: #f7f7f5;
    --gold: #b8862a;
    --navy: #2b2b8a;
    --white: #ffffff;
  }
  * { box-sizing: border-box; margin: 0; padding: 0; }
  html, body {
    width: 1200px;
    height: 800px;
    overflow: hidden;
    background: var(--backdrop);
    font-family: "Source Serif 4", Georgia, serif;
  }
  .canvas {
    position: relative;
    width: 1200px;
    height: 800px;
  }
  .card {
    position: absolute;
    top: 278px;
    width: 418px;
    height: 240px;
    display: flex;
  }
  .card--gold { left: 142px; --panel: var(--gold); --accent: var(--navy); }
  .card--navy { left: 638px; --panel: var(--navy); --accent: var(--gold); }

  .card__brand {
    width: 179px;
    height: 100%;
    background: var(--paper);
    display: flex;
    flex-direction: column;
    align-items: center;
    justify-content: center;
    gap: 10px;
    padding: 0 18px;
  }
  .brand__dot {
    width: 34px;
    height: 34px;
    border-radius: 50%;
    background: var(--navy);
  }
  .brand__name {
    color: var(--navy);
    font-weight: 700;
    font-size: 15px;
    line-height: 1.25;
    text-align: center;
    letter-spacing: 0.5px;
  }

  .card__details {
    flex: 1;
    background: var(--panel);
    color: var(--white);
    padding: 36px 6px 0 23px;
    font-size: 13.5px;
    line-height: 18px;
    white-space: nowrap;
  }
  .details__name {
    color: var(--accent);
    font-weight: 700;
    font-size: 16px;
    line-height: 17px;
  }
  .details__title { margin-bottom: 11px; }
  .details__address { margin-bottom: 9px; }
  .details__label { color: var(--accent); }
  .details__contact { font-size: 12.5px; line-height: 18px; }
</style>
</head>
<body>
<main class="canvas">

  <article class="card card--gold">
    <div class="card__brand">
      <span class="brand__dot"></span>
      <p class="brand__name">Crest of Morning Paddocks</p>
    </div>
    <div class="card__details">
      <p class="details__name">Maren Dunleavy</p>
      <p class="details__title">Director of Operations</p>
      <p class="details__address">27 Ashbrook Lane<br>Middletown, MD. 21584</p>
      <p class="details__contact"><span class="details__label">Tel:</span> (313) 555-0147</p>
      <p class="details__contact"><span class="details__label">Fax:</span> (949) 555-0192</p>
      <p class="details__contact"><span class="details__label">Email:</span> maren@cmpaddocks.example</p>
      <p class="details__contact"><span class="details__label">Web:</span> cmpaddocks.example</p>
    </div>
  </article>

  <article class="card card--navy">
    <div class="card__brand">
      <span class="brand__dot"></span>
      <p class="brand__name">Crest of Morning Paddocks</p>
    </div>
    <div class="card__details">
      <p class="details__name">Maren Dunleavy</p>
      <p class="details__title">Director of Operations</p>
      <p class="details__address">27 Ashbrook Lane<br>Middletown, MD. 21584</p>
      <p class="details__contact"><span class="details__label">Tel:</span> (313) 555-0147</p>
      <p class="details__contact"><span class="details__label">Fax:</span> (949) 555-0192</p>
      <p class="details__contact"><span class="details__label">Email:</span> maren@cmpaddocks.example</p>
      <p class="details__contact"><span class="details__label">Web:</span> cmpaddocks.example</p>
    </div>
  </article>

</main>
</body>
</html>
```